Foot and ankle surgeon requires a website design

I need a website where prospective and established patients can obtain information and then direct them to making appointments. My practice is a highly professional surgical practice specialising in surgery to the foot and ankle. My title is Mr Colin Dravers, Podiatric Foot & Ankle Surgeon. My qualifications are: BSc MSc FACPS
The practice website will require information on: Locations, phone numbers to make appointments, general background on podiatric surgery,
I would like to include information on: my hospital appointments, surgical fellowships held, training programs undertaken, association memberships, publications written, links to useful websites
A page dedicated to common foot conditions would be useful and also a page with referral information including an online registration section that will be sent direct to the receptionist.
Examples of similar websites include:
http://www.jorbellianfeet.com.au/
http://www.quandrilfootsurgeon.com.au/
I will provide files on logo, self photos and my personal training history etc.
Also if there is going to be a background theme I personally am associated with surfing and beach activities, it would be great if this was able to be reflected in the design.
Thank you.

```html
<!DOCTYPE html>
<html lang="en">
<head>
<meta charset="utf-8">
<title>Mr Colin Dravers – Podiatric Foot &amp; Ankle Surgeon</title>
<link href="https://fonts.googleapis.com/css2?family=Open+Sans:wght@400;600;700&family=Crimson+Pro:wght@400&display=swap" rel="stylesheet">
<style>
:root{
  --navy:#0d3f78;
  --orange:#ea7a12;
  --text:#3a3a3a;
  --muted:#666;
  --line:#dcdcdc;
  --white:#fff;
}
*{margin:0;padding:0;box-sizing:border-box}
html,body{width:1151px;height:1200px;overflow:hidden}
body{
  position:relative;
  font-family:"Open Sans",sans-serif;color:var(--text);
  background:linear-gradient(90deg,#e4e6e2 0%,#d9dcd6 10%,#e8e8e4 80%,#b8a996 90%,#a49682 100%);
}
.page{position:absolute;left:117px;top:14px;width:917px;height:1162px;background:#fafafa;box-shadow:0 0 8px rgba(0,0,0,.15)}
.abs{position:absolute}
.header{left:16px;top:26px;width:886px;height:125px;background:var(--white);box-shadow:0 1px 6px rgba(0,0,0,.18)}
.brand{left:40px;top:56px;display:flex;align-items:center;gap:10px}
.brand-dot{width:22px;height:22px;border-radius:50%;background:var(--navy)}
.brand-name{font-size:19px;font-weight:600;color:var(--navy);line-height:1}
.brand-sub{left:72px;top:80px;font-size:10px;color:var(--muted)}
.cta{right:18px;top:20px;text-align:right}
.cta-title{font-size:15px;font-weight:600;color:var(--orange);letter-spacing:.3px}
.cta-sub{font-size:13px;color:#555;margin:3px 95px 8px 0;text-align:right}
.phone{font-size:14.5px;color:#555;font-weight:600;margin-bottom:6px}
.phone span{font-size:12.5px;font-weight:400;margin-left:8px;display:inline-block;width:70px;text-align:left}
.nav{left:16px;top:171px;width:887px;height:43px;background:var(--navy);display:flex}
.nav a{color:var(--white);text-decoration:none;font-size:12px;font-weight:600;line-height:43px;padding:0 13px}
.nav a.active{background:var(--orange);padding:0 24px}
.slider{left:16px;top:239px;width:886px;height:356px;overflow:hidden}
.slide-photo{width:100%;height:100%;background:radial-gradient(ellipse at 45% 40%,#e8cbbf 0%,#efdfd8 35%,#f4eeee 65%,#ebe8ec 100%)}
.arrow{top:160px;width:32px;height:35px;background:rgba(255,255,255,.85);display:flex;align-items:center;justify-content:center}
.caption{left:33px;top:297px;width:408px;height:42px;background:var(--navy);color:var(--white);font-size:19.5px;font-weight:600;line-height:42px;padding-left:20px;letter-spacing:.4px}
.intro{left:19px;top:624px;width:883px;height:211px;background:var(--white);box-shadow:0 1px 6px rgba(0,0,0,.18)}
.lead{left:16px;top:18px;width:855px;font-size:13.5px;line-height:18px;color:#333}
.portrait{left:22px;top:65px;width:156px;height:115px;background:linear-gradient(180deg,#c9cbcf,#b7babe)}
.points{left:206px;top:70px;width:630px;list-style:none;font-family:"Crimson Pro",serif;font-size:12.5px;line-height:16px;color:#555}
.points li{position:relative;padding-left:22px;margin-bottom:22px}
.points li::before{content:"";position:absolute;left:2px;top:6px;width:5px;height:5px;border-radius:50%;background:#999}
.more{right:14px;top:178px;background:var(--navy);color:var(--white);font-size:11px;font-weight:600;padding:3px 8px}
.footer-rule{left:0;top:880px;width:917px;height:4px;border-top:1px solid var(--line);border-bottom:1px solid var(--line)}
.col{top:918px}
.col h3{font-size:13px;font-weight:600;color:#222;margin-bottom:17px}
.col-sep{top:916px;width:1px;height:156px;background:var(--line)}
.links{list-style:none;font-size:12px;color:#555}
.links li{margin-bottom:5px;padding-left:15px;position:relative}
.links li::before{content:"›";position:absolute;left:0;top:-1px;color:#666}
.addr{font-size:11px;line-height:18px;color:#555;padding-left:22px;position:relative;margin-bottom:18px}
.addr svg{position:absolute;left:3px;top:3px}
.field{width:134px;border:1px solid #ccc;font-size:9.5px;color:#777;padding:2px 6px;margin-bottom:6px;height:20px;background:#fff}
.field.msg{height:39px}
.send{width:134px;height:25px;background:var(--orange);color:#fff;font-size:11px;text-align:center;line-height:25px}
.social{width:26px;height:26px;border-radius:3px;margin-bottom:10px}
.bar{left:0;top:1106px;width:916px;height:56px;background:var(--navy);color:var(--white);font-size:11.5px;line-height:56px;text-align:center}
</style>
</head>
<body>
<div class="page">
  <header class="abs header">
    <div class="abs brand"><span class="brand-dot"></span><span class="brand-name">Mr Colin Dravers</span></div>
    <div class="abs brand-sub">Podiatric Foot &amp; Ankle Surgeon</div>
    <div class="abs cta">
      <div class="cta-title">MAKE APPOINTMENT TODAY</div>
      <div class="cta-sub">Call Us Now</div>
      <div class="phone">08 9100 2741<span>(Geraldton)</span></div>
      <div class="phone">08 9100 5862<span>(Kalgoorlie)</span></div>
    </div>
  </header>

  <nav class="abs nav">
    <a class="active" href="#">Home</a><a href="#">Appointments</a><a href="#">Surgical fellowships</a><a href="#">Training programs</a><a href="#">Memberships</a><a href="#">Publications</a><a href="#">Useful websites</a><a href="#">Contact us</a>
  </nav>

  <section class="abs slider">
    <div class="slide-photo" role="img" aria-label="Podiatrist's hands trimming a patient's toenail"></div>
    <div class="abs arrow" style="left:0"><svg width="10" height="14"><path d="M7 2 2 7l5 5" fill="none" stroke="#666" stroke-width="1.6"/></svg></div>
    <div class="abs arrow" style="right:0"><svg width="10" height="14"><path d="M3 2l5 5-5 5" fill="none" stroke="#666" stroke-width="1.6"/></svg></div>
    <div class="abs caption">Working hard to keep you on your feet</div>
  </section>

  <section class="abs intro">
    <p class="abs lead">The Coastline Foot &amp; Ankle Group strive to provide exceptional service and care to all patients, young and old, to ensure they enjoy a pain free lifestyle.</p>
    <div class="abs portrait" role="img" aria-label="Portrait photo of a practice team member"></div>
    <ul class="abs points">
      <li>For those unfamiliar with our services, we are a team of accredited health professionals dealing with the prevention, diagnosis, treatment and rehabilitation of medical and surgical conditions related to feet, ankles and lower limbs.</li>
      <li>The Coastline Foot &amp; Ankle Group have practices based throughout regional Western Australia in Geraldton and Kalgoorlie and offer the following services; sports injuries, foot care, foot orthoses and diabetes care.</li>
    </ul>
    <div class="abs more">Read More</div>
  </section>

  <div class="abs footer-rule"></div>

  <div class="abs col" style="left:20px">
    <h3>LINKS</h3>
    <ul class="links"><li>Home</li><li>About Us</li><li>Contact Us</li><li>FAQ</li><li>Privacy Policy</li></ul>
  </div>
  <div class="abs col-sep" style="left:191px"></div>
  <div class="abs col" style="left:249px">
    <h3>LOCATION</h3>
    <div class="addr"><svg width="9" height="12"><path d="M4.5 11.5C1.5 7 .8 5.8.8 4.3a3.7 3.7 0 0 1 7.4 0c0 1.5-.7 2.7-3.7 7.2z" fill="#999"/><circle cx="4.5" cy="4.3" r="1.4" fill="#fafafa"/></svg>Geraldton, 14 Marine Parade<br>Harbour Medical Centre<br>Shorehaven WA 6530</div>
    <div class="addr"><svg width="9" height="12"><path d="M4.5 11.5C1.5 7 .8 5.8.8 4.3a3.7 3.7 0 0 1 7.4 0c0 1.5-.7 2.7-3.7 7.2z" fill="#999"/><circle cx="4.5" cy="4.3" r="1.4" fill="#fafafa"/></svg>Kalgoorlie, 3/28 Reef Street<br>Goldfields Health Suites<br>Shorehaven WA 6430</div>
  </div>
  <div class="abs col-sep" style="left:448px"></div>
  <div class="abs col" style="left:492px">
    <h3>CONTACT US</h3>
    <div style="margin-left:-3px">
      <div class="field">Name</div>
      <div class="field">Email</div>
      <div class="field msg">Message</div>
      <div class="send">Contact</div>
    </div>
  </div>
  <div class="abs col-sep" style="left:680px"></div>
  <div class="abs col" style="left:737px">
    <h3>STAYING IN TOUCH</h3>
    <div class="social" style="background:#3b5998"></div>
    <div class="social" style="background:#c4c4c4"></div>
    <div class="social" style="background:#c4c4c4"></div>
  </div>

  <footer class="abs bar">Copyright © yourwebsite &nbsp;|&nbsp; Terms &amp; Conditions &nbsp;|&nbsp; Privacy Policy &nbsp;|&nbsp; 12 Tidewater Lane&nbsp; Shorehaven, Australia 6000</footer>
</div>
</body>
</html>
```